My name is Delia Forsythe,I want to create a web page for my personal dog grooming business. The name on the web page can be "Delia's Dog Grooming" I am located in San Antonio Texas. The page would help grow my customer base. Before and after pictures would display the quality of work that I do. On my page I can provide information about myself, my services, and pricing.
Updates

I have updated project to guaranteed pay

Please try to incorporate a schnauzer in an icon or logo. My dog is a schnauzer. THANKS!!!!!!!!!!!!

Target Market(s)

Dog Owners

Industry/Entity Type

Business

Requirements
Must have
• -A spot for before and after pictures.
-An about me section
-A section to make an appointment
Nice to have
• My favorite Color is purple. I think different shades of purple would be nice or purple with a light green

please incorporate a schnauzer in any icon or logo. My dog is a schnauzer.

```html
<!DOCTYPE html>
<html lang="en">
<head>
<meta charset="utf-8">
<title>Delia's Dog Grooming</title>
<link rel="stylesheet" href="https://fonts.googleapis.com/css2?family=Arimo&family=Open+Sans:wght@400;600;700&family=Delius&family=Kaushan+Script&display=swap">
<style>
:root{
  --hero-top:#4a0f5c;
  --hero-mid:#65177d;
  --band:#3f0c50;
  --panel:#2b0737;
  --lower:#33093f;
  --lower-panel:#28062f;
  --footer:#3a0b48;
  --tab:#2d0838;
  --lilac:#c8a9d6;
  --soft:#e2cde9;
  --green:#8fd12b;
  --green-dark:#5f9a12;
  --white:#ffffff;
  --appt:#8d5aa1;
  --appt-head:#7a4590;
  --send:#9a3d86;
}
*{margin:0;padding:0;box-sizing:border-box}
html,body{width:1200px;height:983px;overflow:hidden}
body{position:relative;background:var(--band);font-family:"Open Sans",sans-serif;color:var(--lilac)}
.abs{position:absolute}

.hero{left:0;top:0;width:1200px;height:380px;background:linear-gradient(180deg,var(--hero-top) 0%,var(--hero-mid) 100%)}
.hero-glow{left:560px;top:40px;width:560px;height:400px;background:radial-gradient(ellipse at center,rgba(226,190,240,.55) 0%,rgba(160,90,190,.2) 45%,rgba(101,23,125,0) 70%)}
.logo-blob{left:10px;top:-20px;width:386px;height:161px;border-radius:50%;background:#5b1a72}
.blob-small{left:355px;top:-20px;width:160px;height:80px;border-radius:50%;background:#591a70}
.logo-dog{left:44px;top:21px;width:86px;height:109px;border-radius:8px;background:linear-gradient(160deg,#d8d8d8,#6a6a6a)}
.brand{left:134px;top:44px;color:var(--white);font-family:"Open Sans",sans-serif;font-weight:700;font-size:30px;line-height:34px}
.brand span{display:block;padding-left:56px;font-size:22px;line-height:28px}

.nav{left:578px;top:0;display:flex;gap:0}
.nav a{position:absolute;top:0;height:63px;display:flex;align-items:center;justify-content:center;background:var(--tab);color:var(--white);font-weight:700;font-size:15px;text-decoration:none}
.nav a.active::after{content:"";position:absolute;left:12px;right:12px;bottom:2px;height:2px;background:var(--green)}

.headline{left:130px;top:166px;width:440px;font-family:"Arimo",sans-serif;font-size:32px;line-height:37px;color:#c3a3cf;text-transform:uppercase}
.hero-copy{left:130px;top:293px;width:485px;font-size:12px;line-height:15px;color:var(--soft)}
.btn-green{display:flex;align-items:center;justify-content:center;background:linear-gradient(180deg,#b6ec4a,var(--green) 55%,var(--green-dark));color:#1c2a05;font-weight:700;border-radius:4px}
.read-more{left:481px;top:350px;width:128px;height:28px;font-size:13px;gap:10px}
.slide-arrow{width:42px;height:42px}
.hero-dogs{left:667px;top:151px;width:364px;height:286px;border-radius:40% 40% 20% 20%;background:radial-gradient(ellipse at 50% 45%,#e9a95b 0%,#c7782e 55%,rgba(160,90,40,0) 80%)}

.welcome{left:74px;top:415px;width:1059px;height:259px;background:var(--panel);border-radius:8px}
.welcome-title{left:88px;top:430px;font-family:"Delius",cursive;font-size:29px;color:#e7d6ee;letter-spacing:2px;display:flex;align-items:center;gap:8px}
.welcome-copy{left:122px;top:474px;width:656px;font-size:12.4px;line-height:15.2px;color:var(--soft);letter-spacing:.3px}
.welcome-copy p+p{margin-top:15px}

.appointment{left:853px;top:462px;width:241px;height:171px;background:var(--appt);border-radius:6px;overflow:hidden}
.appointment h2{height:72px;background:var(--appt-head);color:var(--white);font-size:19px;line-height:23px;text-align:center;padding-top:21px;font-weight:700}
.click-here{left:866px;top:574px;width:142px;height:28px;font-size:15px}
.calendar{left:1004px;top:544px;width:82px;height:84px;border-radius:4px;background:linear-gradient(180deg,#6fa7d8 0 16%,#f2f2f2 16%,#cfd3d8)}

.lower{left:0;top:702px;width:1200px;height:236px;background:var(--lower)}
.tab{top:702px;height:30px;width:179px;background:var(--tab);color:#c9a6d8;font-weight:700;font-size:14px;display:flex;align-items:center;justify-content:center}
.photo{top:761px;height:136px;border:1px solid #e6e6e6;background:linear-gradient(160deg,#e9e9ea,#9a9a9e)}
.mini-arrow{width:24px;height:24px}

.contact{left:525px;top:713px;width:608px;height:216px;background:var(--lower-panel);border-radius:6px}
.contact-label{left:550px;top:735px;font-size:14px;color:#cdb8d6}
.message{left:546px;top:766px;width:314px;height:89px;background:#17031c;border:1px solid #4a1a58;padding:10px 12px;font-size:12px;color:#8d4aa8}
.send{left:716px;top:875px;width:144px;height:29px;border-radius:5px;background:linear-gradient(180deg,#c05aa8,var(--send) 55%,#6e2360);color:var(--white);font-size:16px;display:flex;align-items:center;justify-content:center}
.divider{left:894px;top:750px;width:1px;height:148px;background:#5a3468}
.contact-title{left:914px;top:733px;font-family:"Kaushan Script",cursive;font-size:28px;color:var(--white)}
.schnauzer{left:1060px;top:675px;width:132px;height:242px;border-radius:45% 45% 20% 20%;background:linear-gradient(170deg,#cfcfcf,#5a5a5a 70%,rgba(60,20,70,0))}
.social{top:891px;width:28px;height:28px;border-radius:50%;background:#4f4a40;border:2px solid #8a8474;display:flex;align-items:center;justify-content:center}

.stripe{left:0;top:938px;width:1200px;height:8px;background:repeating-linear-gradient(135deg,var(--green) 0 6px,#6ea81c 6px 12px)}
.footer{left:0;top:946px;width:1200px;height:37px;background:var(--footer);color:#c2a4cf;font-size:11px;letter-spacing:.4px;display:flex;align-items:center;justify-content:center}
</style>
</head>
<body>

<div class="abs hero"></div>
<div class="abs hero-glow"></div>
<div class="abs logo-blob"></div>
<div class="abs blob-small"></div>
<div class="abs logo-dog" role="img" aria-label="Photo of a seated schnauzer"></div>
<div class="abs brand">Delia's<span>Dog Grooming</span></div>

<nav class="abs nav">
  <a class="active" href="#" style="left:0;width:122px">About Me</a>
  <a href="#" style="left:128px;width:120px">Services</a>
  <a href="#" style="left:257px;width:120px">Pricing</a>
  <a href="#" style="left:390px;width:130px">Photo Gallery</a>
</nav>

<h1 class="abs headline">No messes in your car, no separation anxiety</h1>
<p class="abs hero-copy">Our copmany utilize the very latest in mobile grooming technology to ensure your best friends visit with us is a safe and happy times.Our copmany utilize the very latest in mobile grooming technology to ensure your best friends visit with us is a safe and happy times.</p>
<a class="abs btn-green read-more" href="#">
  <svg width="22" height="20" viewBox="0 0 22 20"><g fill="#1c2a05"><ellipse cx="11" cy="14" rx="6" ry="5"/><circle cx="4" cy="8" r="2.4"/><circle cx="8" cy="4" r="2.4"/><circle cx="14" cy="4" r="2.4"/><circle cx="18" cy="8" r="2.4"/></g></svg>
  Read more
</a>
<svg class="abs slide-arrow" style="left:51px;top:221px" viewBox="0 0 42 42"><circle cx="21" cy="21" r="20" fill="#8fd12b" stroke="#5f9a12" stroke-width="2"/><path d="M25 12 L14 21 L25 30 Z" fill="#fff"/></svg>
<svg class="abs slide-arrow" style="left:1112px;top:221px" viewBox="0 0 42 42"><circle cx="21" cy="21" r="20" fill="#8fd12b" stroke="#5f9a12" stroke-width="2"/><path d="M17 12 L28 21 L17 30 Z" fill="#fff"/></svg>

<div class="abs welcome"></div>
<div class="abs hero-dogs" role="img" aria-label="Photo of two golden puppies sitting side by side"></div>
<h2 class="abs welcome-title">
  <svg width="26" height="24" viewBox="0 0 22 20"><g fill="#e7d6ee"><ellipse cx="11" cy="14" rx="6" ry="5"/><circle cx="4" cy="8" r="2.4"/><circle cx="8" cy="4" r="2.4"/><circle cx="14" cy="4" r="2.4"/><circle cx="18" cy="8" r="2.4"/></g></svg>
  Welcome
</h2>
<div class="abs welcome-copy">
  <p>Don't forget to check free website templates every day, because we add a new free website template almost daily.You can remove any link to our websites from this template you're free to use the tem-plate without linking back to us. This is just a place holder so you can see how the site would look like.Don't forget to check free website templates every day, because we add a new free website tem-plate almost daily.You can remove any link to our websites from this template you're free to use the template without linking back to us.This is just a place holder so you can see how the site would look like.</p>
  <p>You can remove any link to our websites from this template you're free to use the template without linking back to us.This is just a place holder so you can see how the site would look like.</p>
</div>

<section class="abs appointment"><h2>Make an<br>Appointment</h2></section>
<a class="abs btn-green click-here" href="#">Click Here</a>
<div class="abs calendar" role="img" aria-label="Calendar and clock icon"></div>

<div class="abs lower"></div>
<div class="abs tab" style="left:74px">Before Grooming</div>
<div class="abs tab" style="left:270px">After Grooming</div>
<svg class="abs mini-arrow" style="left:59px;top:817px" viewBox="0 0 24 24"><circle cx="12" cy="12" r="11" fill="#8fd12b" stroke="#5f9a12"/><path d="M14 7 L8 12 L14 17 Z" fill="#fff"/></svg>
<div class="abs photo" style="left:107px;width:131px" role="img" aria-label="Before grooming photo of a shaggy white terrier"></div>
<div class="abs photo" style="left:294px;width:125px" role="img" aria-label="After grooming photo of a neatly trimmed white terrier"></div>
<svg class="abs mini-arrow" style="left:444px;top:813px" viewBox="0 0 24 24"><circle cx="12" cy="12" r="11" fill="#8fd12b" stroke="#5f9a12"/><path d="M10 7 L16 12 L10 17 Z" fill="#fff"/></svg>

<div class="abs contact"></div>
<p class="abs contact-label">I'd also like to leave a message for you:</p>
<div class="abs message">Your message</div>
<a class="abs send" href="#">Send enquiry</a>
<div class="abs divider"></div>
<h2 class="abs contact-title">Contact Us</h2>
<div class="abs schnauzer" role="img" aria-label="Photo of a sitting schnauzer"></div>
<span class="abs social" style="left:976px"></span>
<span class="abs social" style="left:1012px"><svg width="14" height="10" viewBox="0 0 14 10"><rect x=".5" y=".5" width="13" height="9" fill="#fff"/><path d="M.5 .5 L7 6 L13.5 .5" fill="none" stroke="#4f4a40"/></svg></span>
<span class="abs social" style="left:1049px"></span>
<span class="abs social" style="left:1088px"></span>

<div class="abs stripe"></div>
<footer class="abs footer">COPYRIGHT © 2011 DELIAGROOMS.COM. ALL RIGHTS RESERVED</footer>

</body>
</html>
```